NEW Escape Room. Fun, Dark and Mysterious.

Escape Room Website. Bookings and scheduling of appointments will be organised with Bolkit through the site. Most appointments will be created online through the booking system with some payments coming through in person by drop-ins. Groups will be from 2 - 8 people with a sliding scale of prices. We will start with one game playable and one saying coming soon. We will also eventually have 4 games up and running at once so will need it to be able to expand. We don't have any images of the rooms because it all relies heavily on mystery. Appointments are each 1 hour long with 30 minutes in between.

Target Market(s)

15-35 year olds

Coding

Coded - Design and coding required

Number of Pages Required

5+ page

Font styles to use
Decorative

Colors

Designer to choose colors to be used in the design.

Requirements
Must have
• Graphics showing what an escape room is.
• Page for About - What is an escape room
• Page for Games - Showing each of the different games which can be played with links to booking page. We have one game to start - the tailor's shadows. A victorian doctors office and serial killers. Then a game coming soon which is aztec/mayan/jungle/captain Worrel feel.
• FAQ Page
Nice to have
• Graphics for multiple players ie 2 players, 3 players, 4 players etc
• Dark and Mysterious feel.
• Inspiration from Cipher Vault, Lockwise Hall, Puzzle Harbor
Should not have
• Cartoony/childish. Pink.
• Not bloody or dripping letters etc - not cliche.
• Not horror themed.

```html
<!DOCTYPE html>
<html lang="en">
<head>
<meta charset="utf-8">
<title>The Hollow Key – Escape Rooms</title>
<link rel="stylesheet" href="https://fonts.googleapis.com/css2?family=Special+Elite&family=Poppins:wght@400;500;600&family=Lato:wght@300;400&display=swap">
<style>
:root{
  --bg:#1c1c1c;
  --bg-foot:#181818;
  --bar:#0e0e0e;
  --orange:#c45a24;
  --text:#f2f2f2;
  --muted:#bdbdbd;
  --dim:#9a9a9a;
  --line:#d9d9d9;
}
*{margin:0;padding:0;box-sizing:border-box}
html,body{width:1200px;height:2540px;overflow:hidden}
body{background:var(--bg);color:var(--text);font-family:'Lato',sans-serif;position:relative}
.abs{position:absolute}
.display{font-family:'Special Elite','Courier New',monospace;font-weight:400}
.accent{color:var(--orange)}

/* hero */
.hero{left:0;top:0;width:1200px;height:650px;
  background:radial-gradient(ellipse at 38% 30%,#5a5a55 0%,#3a3a37 22%,#232322 50%,#1c1c1c 80%),
  linear-gradient(#2a2a28,#1c1c1c)}
.hero-door{left:290px;top:120px;width:280px;height:480px;border-radius:140px 140px 0 0;
  background:linear-gradient(#8c8c86,#4b4b47 60%,#2a2a28)}
.hero-shade{left:0;top:0;width:1200px;height:650px;background:linear-gradient(rgba(28,28,28,.35),rgba(28,28,28,.2) 50%,#1c1c1c 100%)}
.brand{font-family:'Special Elite','Courier New',monospace;color:var(--orange);font-size:20px;display:flex;align-items:center;gap:10px;white-space:nowrap}
.brand .mark{width:18px;height:18px;border-radius:50%;background:var(--orange);flex:none}
.nav{left:269px;top:68px;display:flex;gap:54px;font-family:'Poppins',sans-serif;font-size:13px;font-weight:500}
.nav a{color:var(--text);text-decoration:none}
.btn{background:var(--orange);color:#fff;font-family:'Poppins',sans-serif;font-weight:600;font-size:13px;border-radius:20px;display:flex;align-items:center;justify-content:center}
.book{left:851px;top:60px;width:107px;height:37px}
.tools{left:992px;top:68px;display:flex;align-items:center;gap:14px;font-family:'Poppins',sans-serif;font-size:13px;font-weight:500}
.tools .sep{width:1px;height:14px;border-left:1px dotted #888}
.hero-title{left:0;top:318px;width:1200px;text-align:center;font-size:76px;letter-spacing:1px;white-space:nowrap}
.dots{left:571px;top:591px;display:flex;gap:16px}
.dots span{width:9px;height:9px;border-radius:50%;background:#8a8a8a}
.dots span:first-child{background:var(--orange)}

.section-title{width:1200px;left:0;text-align:center;font-size:50px}

/* players */
.hex-row{left:0;top:800px;width:1200px;height:170px}
.player-label{top:980px;width:200px;text-align:center;font-family:'Special Elite','Courier New',monospace;font-size:21px}

/* cards */
.card{top:1183px;width:318px}
.card-photo{height:210px}
.card h3{font-family:'Special Elite','Courier New',monospace;font-weight:400;font-size:27px;margin-top:14px}
.card p{font-size:14px;line-height:19.5px;color:var(--muted);margin-top:4px;font-weight:300}
.card .more{font-family:'Special Elite','Courier New',monospace;color:var(--orange);font-size:15px;margin-top:10px;display:block}

/* contact */
.contact-photo{left:0;top:1680px;width:410px;height:420px;
  background:radial-gradient(ellipse at 45% 45%,#5a5650 0%,#333230 35%,#1f1f1f 70%,#1c1c1c 100%)}
.field{border:1px solid var(--line);border-radius:22px;height:45px;padding:0 16px;display:flex;align-items:center;font-size:14px;color:#ddd}
.message{left:430px;top:1897px;width:678px;height:166px;border:1px solid var(--line);border-radius:6px;padding:12px 16px;font-size:14px;color:#ddd}
.send{left:1000px;top:2076px;width:108px;height:37px;font-size:14px}

/* footer */
.footer{left:0;top:2165px;width:1200px;height:325px;background:var(--bg-foot)}
.foot-col{top:2256px}
.foot-col h4{font-family:'Special Elite','Courier New',monospace;font-weight:400;font-size:18px;margin-bottom:18px}
.foot-col li{list-style:none;font-size:13px;color:var(--dim);margin-bottom:13px;display:flex;gap:12px;align-items:flex-start;line-height:15px}
.foot-col .ico{width:16px;flex:none;display:flex;justify-content:center}
.social-dot{width:12px;height:12px;border-radius:50%;background:var(--orange);margin-top:1px}
.bottom-bar{left:0;top:2490px;width:1200px;height:50px;background:var(--bar);display:flex;align-items:center;justify-content:center;font-family:'Special Elite','Courier New',monospace;font-size:12px}
</style>
</head>
<body>

<header>
  <div class="abs hero" role="img" aria-label="Dim abandoned room with an arched window and light falling through an open door"></div>
  <div class="abs hero-door" role="img" aria-label="Arched window and doorway glowing faintly"></div>
  <div class="abs hero-shade"></div>

  <div class="abs brand" style="left:94px;top:66px;font-size:16px"><span class="mark"></span>The Hollow Key</div>
  <nav class="abs nav">
    <a href="#">Home</a><a href="#">About</a><a href="#">Games</a><a href="#">FAQ</a><a href="#">Contact Us</a>
  </nav>
  <div class="abs btn book">Book Now!</div>
  <div class="abs tools">
    <svg width="14" height="14" viewBox="0 0 14 14" fill="none" stroke="#fff" stroke-width="1.6"><circle cx="6" cy="6" r="4.5"/><path d="M9.5 9.5L13 13"/></svg>
    <span class="sep"></span>
    <svg width="13" height="14" viewBox="0 0 13 14" fill="none" stroke="#fff" stroke-width="1.4"><circle cx="6.5" cy="4" r="3"/><path d="M1 13.5c0-3 2.5-5 5.5-5s5.5 2 5.5 5"/></svg>
    <span style="margin-left:-8px">Signup</span>
  </div>

  <h1 class="abs hero-title display"><span class="accent">T</span>he <span class="accent">H</span>ollow <span class="accent">K</span>ey</h1>
  <div class="abs dots"><span></span><span></span><span></span></div>
</header>

<section>
  <h2 class="abs section-title display" style="top:678px"><span class="accent">W</span>hat an Escape Room Is</h2>
  <svg class="abs hex-row" viewBox="0 0 1200 170" fill="none" stroke="#c45a24">
    <path d="M368 86H537M666 86H830" stroke-width="2" stroke-dasharray="2 3"/>
    <g stroke-width="5">
      <polygon points="305,12 368,48 368,122 305,158 242,122 242,48"/>
      <polygon points="600,12 663,48 663,122 600,158 537,122 537,48"/>
      <polygon points="898,12 961,48 961,122 898,158 835,122 835,48"/>
    </g>
    <g stroke-width="2">
      <path d="M340 4l-12 14M348 4l-12 14M356 4l-12 14M262 150l-12 14M270 150l-12 14"/>
      <path d="M635 4l-12 14M643 4l-12 14M651 4l-12 14M557 150l-12 14M565 150l-12 14"/>
      <path d="M933 4l-12 14M941 4l-12 14M949 4l-12 14M855 150l-12 14M863 150l-12 14"/>
      <circle cx="290" cy="73" r="9"/><circle cx="320" cy="73" r="9"/>
      <path d="M272 105c0-12 8-20 18-20s18 8 18 20zM302 105c0-12 8-20 18-20s18 8 18 20z"/>
      <circle cx="580" cy="70" r="7"/><circle cx="600" cy="67" r="8"/><circle cx="620" cy="70" r="7"/>
      <path d="M566 100c0-10 6-18 14-18M634 100c0-10-6-18-14-18M584 102c0-12 7-20 16-20s16 8 16 20z"/>
      <circle cx="898" cy="52" r="6"/><circle cx="874" cy="78" r="6"/><circle cx="922" cy="78" r="6"/><circle cx="898" cy="102" r="6"/>
      <path d="M888 70c0-6 4-10 10-10s10 4 10 10zM864 96c0-6 4-10 10-10s10 4 10 10zM912 96c0-6 4-10 10-10s10 4 10 10zM888 120c0-6 4-10 10-10s10 4 10 10z"/>
      <rect x="886" y="80" width="24" height="12"/>
    </g>
  </svg>
  <div class="abs player-label" style="left:205px">2 Players</div>
  <div class="abs player-label" style="left:500px">3 Players</div>
  <div class="abs player-label" style="left:798px">4 Players</div>
</section>

<section>
  <h2 class="abs section-title display" style="top:1104px"><span class="accent">W</span>ho Can Play</h2>
  <article class="abs card" style="left:94px">
    <div class="card-photo" role="img" aria-label="Family solving a puzzle at a barred escape room door" style="background:linear-gradient(120deg,#5c4f43,#8a7a66 45%,#c9a566)"></div>
    <h3><span class="accent">F</span>amily</h3>
    <p>Maecenas eros est, finibus nec elit quis, sollicitudin pulvinar ligula. Ut venenatis dapibus metus, vitae mollis ex efficitur ut. Donec sed molestie velit.</p>
    <span class="more">Read More</span>
  </article>
  <article class="abs card" style="left:441px">
    <div class="card-photo" role="img" aria-label="Colleagues escaping through a narrow locked doorway" style="background:linear-gradient(120deg,#3b3b3d,#7a7a7c 50%,#c9c8c6)"></div>
    <h3><span class="accent">C</span>orporate</h3>
    <p>Maecenas eros est, finibus nec elit quis, sollicitudin pulvinar ligula. Ut venenatis dapibus metus, vitae mollis ex efficitur ut. Donec sed molestie velit.</p>
    <span class="more">Read More</span>
  </article>
  <article class="abs card" style="left:788px">
    <div class="card-photo" role="img" aria-label="Friends searching for clues on the floor of a dark room" style="background:radial-gradient(ellipse at 55% 20%,#6b7690,#2c2a2a 55%,#1a1816)"></div>
    <h3><span class="accent">F</span>riends</h3>
    <p>Maecenas eros est, finibus nec elit quis, sollicitudin pulvinar ligula. Ut venenatis dapibus metus, vitae mollis ex efficitur ut. Donec sed molestie velit.</p>
    <span class="more">Read More</span>
  </article>
</section>

<section>
  <div class="abs contact-photo" role="img" aria-label="Hand reaching out from a cobwebbed dark door"></div>
  <h2 class="abs display" style="left:430px;top:1704px;font-size:50px"><span class="accent">G</span>et In Touch</h2>
  <div class="abs field" style="left:430px;top:1784px;width:335px">Name</div>
  <div class="abs field" style="left:772px;top:1784px;width:335px">Email</div>
  <div class="abs field" style="left:430px;top:1840px;width:335px">Phone</div>
  <div class="abs field" style="left:772px;top:1840px;width:335px">Location</div>
  <div class="abs message">Message</div>
  <div class="abs btn send">Send Now</div>
</section>

<footer>
  <div class="abs footer"></div>
  <div class="abs brand" style="left:94px;top:2330px;font-size:18px"><span class="mark"></span>The Hollow Key</div>

  <div class="abs foot-col" style="left:338px">
    <h4>Quick Links</h4>
    <ul><li>Home</li><li>About</li><li>Games</li><li>FAQ</li><li>Contact Us</li></ul>
  </div>
  <div class="abs foot-col" style="left:532px">
    <h4>Contact</h4>
    <ul>
      <li><span class="ico"><svg width="13" height="16" viewBox="0 0 13 16"><path d="M6.5 0A6 6 0 0 0 .5 6c0 4.5 6 10 6 10s6-5.5 6-10a6 6 0 0 0-6-6z" fill="#c45a24"/><circle cx="6.5" cy="6" r="2.3" fill="#181818"/></svg></span><span>48 Lantern Row<br>Ashford Vale</span></li>
      <li><span class="ico"><svg width="14" height="14" viewBox="0 0 14 14"><path d="M3 1l2.5 3-1.5 2c1 2 2 3 4 4l2-1.5 3 2.5-1.5 2C6 13 1 8 1 2.5z" fill="#c45a24"/></svg></span><span>+1 555-014-2290</span></li>
      <li><span class="ico"><svg width="16" height="12" viewBox="0 0 16 12"><rect x="0" y="0" width="16" height="12" fill="#c45a24"/><path d="M0 0l8 6 8-6" stroke="#181818" stroke-width="1.2" fill="none"/></svg></span><span>hello@hollowkeyrooms</span></li>
    </ul>
  </div>
  <div class="abs foot-col" style="left:788px">
    <h4>Games</h4>
    <ul><li>The Tailor's Shadows</li><li>Jaguar's Tomb</li></ul>
  </div>
  <div class="abs foot-col" style="left:998px">
    <h4>Follow Us</h4>
    <ul>
      <li><span class="ico"><span class="social-dot"></span></span>Circlebook</li>
      <li><span class="ico"><span class="social-dot"></span></span>Photoreel</li>
      <li><span class="ico"><span class="social-dot"></span></span>Chirpline</li>
      <li><span class="ico"><span class="social-dot"></span></span>Streamtube</li>
    </ul>
  </div>

  <div class="abs bottom-bar">© 2020&nbsp;<span class="accent">The Hollow Key.</span>&nbsp;All Rights Reserved.</div>
</footer>

</body>
</html>
```